Professional, Modern and Clean Business Card
Brightvale Grocers & Supply Partners, Inc.
Professional, Modern and Clean Business Card - Food
Creative Brief
Simple
Dorian Whitcombe
71-14 82nd Avenue Maspeth, NY 11492
dorian@brightvalegrocers.example
www.brightvalegrocers.example
We will need 2 business cards, one for myself Dorian Whitcombe and the other Rowan Elkhart. My information is above, for Rowan Elkhart the cell is (214) 555-0193 and the email is row@brightvalegrocers.example, everything else will remain the same.
Be creative with just the logo on the back.

```html
<!DOCTYPE html>
<html lang="en">
<head>
<meta charset="utf-8">
<title>Brightvale Grocers – Business Card</title>
<link rel="stylesheet" href="https://fonts.googleapis.com/css2?family=Open+Sans:wght@300;400;700&display=swap">
<style>
  :root {
    --backdrop: #d9d7d3;
    --card: #f7f7f6;
    --brand-red: #e0323c;
    --band-dark: #e23a43;
    --band-light: #f47c82;
    --text-white: #ffffff;
    --text-dark: #4a4a4a;
  }
  * { box-sizing: border-box; margin: 0; padding: 0; }
  html, body {
    width: 1200px;
    height: 940px;
    overflow: hidden;
    background: var(--backdrop);
    font-family: "Open Sans", Arial, sans-serif;
  }
  .card {
    position: absolute;
    left: 320px;
    top: 45px;
    width: 560px;
    height: 850px;
    background: var(--card);
    border-radius: 36px;
    box-shadow: 0 6px 18px rgba(0,0,0,0.18);
    overflow: hidden;
  }
  .brand {
    position: absolute;
    top: 205px;
    left: 0;
    width: 100%;
    text-align: center;
    font-size: 64px;
    font-weight: 700;
    color: var(--brand-red);
    letter-spacing: 0.5px;
  }
  .band-rule {
    position: absolute;
    left: 0;
    width: 100%;
    height: 6px;
    background: var(--brand-red);
  }
  .band-rule.top { top: 372px; }
  .band-rule.bottom { top: 556px; }
  .name-band {
    position: absolute;
    top: 388px;
    left: 0;
    width: 100%;
    height: 158px;
    background: linear-gradient(90deg, var(--band-dark) 0%, var(--band-light) 60%, var(--band-dark) 100%);
    padding: 38px 0 0 110px;
    color: var(--text-white);
  }
  .person-name {
    font-size: 38px;
    font-weight: 300;
    letter-spacing: 1px;
    text-transform: uppercase;
  }
  .person-title {
    font-size: 27px;
    font-weight: 300;
    margin-top: 4px;
  }
  .contact {
    position: absolute;
    top: 600px;
    left: 110px;
    list-style: none;
    color: var(--text-dark);
    font-size: 21px;
    line-height: 38px;
  }
</style>
</head>
<body>
  <div class="card">
    <div class="brand">Brightvale</div>
    <div class="band-rule top"></div>
    <div class="name-band">
      <div class="person-name">Dorian Whitcombe</div>
      <div class="person-title">Managing Director</div>
    </div>
    <div class="band-rule bottom"></div>
    <ul class="contact">
      <li>71-14 82nd Avenue Maspeth, NY 11492</li>
      <li>(214) 555-0147</li>
      <li>dorian@brightvalegrocers.example</li>
      <li>www.brightvalegrocers.example</li>
    </ul>
  </div>
</body>
</html>
```